Kestra Rowe - Contact/Landing Page

I need a landing page which will essentially be the page that customers will go to from the 'website' link on TLX listing. It will provide a short overview of services which need to be selectable. a little further down can capture some contact details followed by a large Submit Now button etc...

I have some icon/logo's that can be utilised at the bottom of the page as industry type references.

Target Market(s)

End of Lease Cleaning Services

Industry/Entity Type

Cleaning Service

Colors

Designer to choose colors to be used in the design.

Requirements
Must have
• As per description
Should not have
• Colours to match my website kestrarowe.com.au

```html
<!DOCTYPE html>
<html lang="en">
<head>
<meta charset="utf-8">
<title>Kestra Rowe – End of Lease Services</title>
<link href="https://fonts.googleapis.com/css2?family=Mulish:ital,wght@0,400;0,600;0,700;1,800&display=swap" rel="stylesheet">
<style>
:root{
  --blue:#1f9ad8;
  --blue-deep:#1a86cc;
  --hero-a:#8cc0e4;
  --hero-b:#5f9fcf;
  --ink:#1d1d1f;
  --text:#2b2b2b;
  --muted:#6a6a6a;
  --line:#c9c9c9;
  --dash:#7dc0ea;
  --footer:#222831;
  --white:#ffffff;
  --photo-1:#b9ad96;
  --photo-2:#8f9296;
  --photo-3:#d9c9b4;
}
*{box-sizing:border-box;margin:0;padding:0}
html,body{width:694px;height:1200px;overflow:hidden}
body{position:relative;background:var(--white);font-family:'Mulish',sans-serif;color:var(--text)}
.abs{position:absolute}

.hero{left:0;top:0;width:694px;height:253px;background:linear-gradient(120deg,var(--hero-a),var(--hero-b))}
.brand{left:0;top:95px;width:694px;display:flex;justify-content:center;align-items:center;gap:10px}
.brand-dot{width:22px;height:22px;border-radius:50%;background:var(--blue-deep)}
.brand-name{font-size:30px;font-weight:700;color:var(--blue-deep)}
.hero-title{left:0;top:196px;width:694px;text-align:center;font-size:23px;font-weight:800;font-style:italic;color:#253746}

.service-photo{top:274px;width:152px;height:160px;border:2px solid #8d8d8d;outline:1px solid #fff;outline-offset:-4px}
.service-name{top:440px;font-size:14px;font-weight:600;color:var(--ink)}
.service-desc{top:463px;font-size:9.4px;line-height:14.4px;color:var(--text);width:150px}
.select{top:509px;display:flex;align-items:center;gap:8px;font-size:11px;color:var(--ink)}
.select.on{color:var(--blue)}
.box{width:18px;height:18px;border:1px solid #555;background:#fff}

.form-card{left:143px;top:569px;width:408px;height:217px;background:#fff;box-shadow:0 3px 6px rgba(0,0,0,.18);border-radius:3px}
.dash{left:176px;width:342px;height:2px;background:repeating-linear-gradient(90deg,var(--dash) 0 14px,transparent 14px 25px)}
.form-title{left:143px;top:584px;width:408px;text-align:center;font-size:19px;font-weight:800;font-style:italic;color:#000}
.field{height:24px;border:1px solid var(--line);border-radius:3px;display:flex;align-items:flex-start;font-size:6.6px;color:#555}
.field .ico{width:20px;height:100%;border-right:1px solid var(--line);display:flex;align-items:center;justify-content:center;max-height:22px;margin-top:0}
.field .ph{padding:8px 0 0 7px}
.field.tall{height:49px}
.field.tall .ico{height:16px;margin-top:3px}
.field.tall .ph{padding-top:6px}
.submit{left:313px;top:745px;width:67px;height:23px;border-radius:12px;background:var(--blue);color:#fff;font-size:10.5px;font-weight:700;display:flex;align-items:center;justify-content:center}

.accr-title{left:0;top:827px;width:694px;text-align:center;font-size:19px;font-weight:800;font-style:italic;color:#000}
.badge{width:147px;height:81px;background:#fff;box-shadow:0 0 3px rgba(0,0,0,.12);display:flex;align-items:center;justify-content:center}
.badge-mark{width:126px;height:52px;border-radius:4px}
.licence{font-size:7px;color:#222}

.footer{left:0;top:1085px;width:694px;height:90px;background:var(--footer)}
.contact{top:1114px;display:flex;align-items:center;gap:7px;color:#fff}
.contact .circle{width:31px;height:31px;border-radius:50%;background:var(--blue);display:flex;align-items:center;justify-content:center;flex:none}
.contact .label{font-size:8.4px;color:#e9e9e9}
.contact .value{font-size:7.4px;line-height:12px;color:#e9e9e9}
.copyright{left:0;top:1175px;width:694px;height:25px;background:var(--blue-deep);color:#e8f2fb;font-size:7.4px;display:flex;align-items:center;justify-content:center}
.copyright b{font-weight:700;color:#fff;margin:0 2px}
</style>
</head>
<body>

<header class="hero abs" role="img" aria-label="Bright empty room with staircase and glass doors, tinted blue"></header>
<div class="brand abs"><span class="brand-dot"></span><span class="brand-name">Kestra Rowe</span></div>
<h1 class="hero-title abs">End of Lease Services</h1>

<section class="services">
  <div class="service-photo abs" style="left:108px;background:linear-gradient(135deg,#d8d0c0,var(--photo-1))" role="img" aria-label="Cleaner mopping a living room floor beside a bucket of supplies"></div>
  <div class="service-photo abs" style="left:271px;background:linear-gradient(135deg,#c8c9cb,var(--photo-2))" role="img" aria-label="Carpet being steam cleaned with a wand"></div>
  <div class="service-photo abs" style="left:434px;background:linear-gradient(135deg,#ece4d8,var(--photo-3))" role="img" aria-label="Technician spraying for pests under a couch"></div>

  <h2 class="service-name abs" style="left:110px">Property Cleaning</h2>
  <p class="service-desc abs" style="left:111px">All interior Cleaning carried out to property&nbsp; Management requirements</p>
  <div class="select on abs" style="left:109px">Select
    <svg width="14" height="13" viewBox="0 0 14 13"><rect x="1" y="2" width="10" height="10" fill="none" stroke="#1f9ad8" stroke-width="1.6"/><path d="M3.5 6.5l3 3L13 1.5" fill="none" stroke="#1f9ad8" stroke-width="2"/></svg>
  </div>

  <h2 class="service-name abs" style="left:273px">Carpet Cleaning</h2>
  <p class="service-desc abs" style="left:273px">Carpet Steam Cleaning to Australian Standard AS 3733:1995</p>
  <div class="select abs" style="left:276px">Select <span class="box"></span></div>

  <h2 class="service-name abs" style="left:440px">Pest Control</h2>
  <p class="service-desc abs" style="left:440px;width:160px">Mandatory Requirement&nbsp; for pets on premises</p>
  <div class="select abs" style="left:443px">Select <span class="box"></span></div>
</section>

<section class="form">
  <div class="form-card abs"></div>
  <div class="dash abs" style="top:568px"></div>
  <div class="dash abs" style="top:784px"></div>
  <h2 class="form-title abs">Submit Your Details</h2>

  <div class="field abs" style="left:175px;top:621px;width:167px">
    <span class="ico"><svg width="7" height="7" viewBox="0 0 8 8"><circle cx="4" cy="2.2" r="2" fill="#1f9ad8"/><path d="M0 8c0-3 1.5-3.6 4-3.6S8 5 8 8z" fill="#1f9ad8"/></svg></span><span class="ph">First Name*</span></div>
  <div class="field abs" style="left:351px;top:621px;width:167px">
    <span class="ico"><svg width="7" height="7" viewBox="0 0 8 8"><circle cx="4" cy="2.2" r="2" fill="#1f9ad8"/><path d="M0 8c0-3 1.5-3.6 4-3.6S8 5 8 8z" fill="#1f9ad8"/></svg></span><span class="ph">Last Name*</span></div>
  <div class="field abs" style="left:175px;top:653px;width:167px">
    <span class="ico"><svg width="7" height="7" viewBox="0 0 8 8"><path d="M1 0.5l2 0 0.8 2-1.2 1c0.5 1 1 1.6 2 2l1-1.2 2 0.8v2C4 7.5 0.5 4 1 0.5z" fill="#1f9ad8"/></svg></span><span class="ph">Your Phone*</span></div>
  <div class="field abs" style="left:351px;top:653px;width:167px">
    <span class="ico"><svg width="8" height="6" viewBox="0 0 8 6"><rect width="8" height="6" fill="#1f9ad8"/><path d="M0 0l4 3 4-3" fill="none" stroke="#fff" stroke-width=".8"/></svg></span><span class="ph">Your Email*</span></div>
  <div class="field tall abs" style="left:175px;top:685px;width:343px">
    <span class="ico"><svg width="8" height="7" viewBox="0 0 8 7"><ellipse cx="3.3" cy="2.6" rx="3.3" ry="2.4" fill="#1f9ad8"/><ellipse cx="5" cy="4.2" rx="3" ry="2.2" fill="#1f9ad8"/></svg></span><span class="ph">Suburb</span></div>

  <div class="submit abs">Submit</div>
</section>

<section class="accreditations">
  <h2 class="accr-title abs">Our Accreditations</h2>
  <div class="badge abs" style="left:109px;top:860px"><span class="badge-mark" style="background:#111"></span></div>
  <div class="badge abs" style="left:274px;top:860px"><span class="badge-mark" style="background:#c9d3e8"></span></div>
  <div class="badge abs" style="left:439px;top:860px"><span class="badge-mark" style="background:#1b3a8a;width:98px"></span></div>
  <div class="badge abs" style="left:191px;top:963px"><span class="badge-mark" style="background:#8cbf3a;height:41px;width:135px;border-radius:0"></span></div>
  <div class="badge abs" style="left:356px;top:963px;flex-direction:column;gap:6px">
    <span class="badge-mark" style="background:#1d2f6b;height:40px;width:126px"></span>
    <span class="licence">Pest Licence : 4817305</span>
  </div>
</section>

<footer>
  <div class="footer abs"></div>
  <div class="contact abs" style="left:113px">
    <span class="circle"><svg width="14" height="14" viewBox="0 0 14 14"><path d="M2 1.5l3 0 1 3-1.6 1.3c.8 1.6 1.8 2.6 3.3 3.3L9 7.5l3 1v3C6 12 1.5 7.5 2 1.5z" fill="none" stroke="#fff" stroke-width="1"/></svg></span>
    <div><div class="label">PHONE</div><div class="value">0400 555 123</div></div>
  </div>
  <div class="contact abs" style="left:240px;top:1114px">
    <span class="circle"><svg width="12" height="15" viewBox="0 0 12 15"><path d="M6 14s5-5 5-8.5A5 5 0 0 0 1 5.5C1 9 6 14 6 14z" fill="none" stroke="#fff" stroke-width="1"/><circle cx="6" cy="5.5" r="1.8" fill="none" stroke="#fff" stroke-width="1"/></svg></span>
    <div><div class="label" style="font-size:7.4px">SERVING</div><div class="value">Parramatta, Baulkham Hills, Mount Druitt,<br>Seven Hills, Blacktown, Penrith,Hills District.</div></div>
  </div>
  <div class="contact abs" style="left:459px">
    <span class="circle"><svg width="15" height="13" viewBox="0 0 15 13"><rect x="1" y="3" width="13" height="9" fill="none" stroke="#fff" stroke-width="1"/><path d="M1 3l6.5 5L14 3M3 1h9v4" fill="none" stroke="#fff" stroke-width="1"/></svg></span>
    <div><div class="label">EMAIL</div><div class="value">info@kestrarowe.com.au</div></div>
  </div>
  <div class="copyright abs">Copyright © 2021 <b>Kestra Rowe.</b> All Rights Reserved.</div>
</footer>

</body>
</html>
```